Luxury new home community needs a contemporary and high end looking brochure

We need a brochure to introduce a luxury new home community. The brochure needs to have a modern and high end look and feel while still keeping nature a predominant theme.
The "purpose.doc" describes the text and must have images for each page. The "BrandGuidelines.pdf" includes the color palette. The "11x17 halffold-inside.jpg and 11x17halffold-outside.jpg" files include the print guidelines that must be met.
The additional images downloaded can be used at your discretion-be creative! I prefer Photoshop files please. Additional information about our new home community can be found at www.MaplecrestHollowNB.com

Target Market(s)

High Net Worth Individuals
Real Estate Agents

Industry/Entity Type

Real Estate

Requirements
Must have
• Please see Purpose.doc for required text and images
• Please see BrandGuidelines.pdf for color palette and fonts

```html
<!DOCTYPE html>
<html lang="en">
<head>
<meta charset="utf-8">
<title>Maplecrest Hollow Brochure</title>
<link rel="stylesheet" href="https://fonts.googleapis.com/css2?family=Open+Sans:wght@400;600;700&display=swap">
<style>
:root{
  --bg:#e8e8e6;
  --brown:#574b42;
  --brown-dark:#3b2f28;
  --band:#8e8a87;
  --band-light:#b9b6b3;
  --paper:#ffffff;
  --paper-soft:#f1f1f0;
  --ink:#3a3632;
  --ink-soft:#6c6661;
  --accent:#7b6a5c;
}
*{margin:0;padding:0;box-sizing:border-box}
html,body{width:1200px;height:2456px;overflow:hidden;background:var(--bg);font-family:"Open Sans",Arial,sans-serif;color:var(--ink)}
.canvas{position:relative;width:1200px;height:2456px}
.page{position:absolute;width:430px;height:560px;background:var(--paper);overflow:hidden;box-shadow:0 2px 6px rgba(0,0,0,.15)}
.spread{position:absolute;width:860px;height:560px;left:170px}
.spread .page{top:0}
.spread .page.left{left:0}
.spread .page.right{left:430px}

/* cover */
.cover-head{height:128px;background:var(--brown);display:flex;align-items:center;justify-content:center;gap:14px}
.brand-mark{width:34px;height:34px;background:var(--paper)}
.brand-name{color:var(--paper);font-weight:600;font-size:25px;letter-spacing:1.5px}
.tagline{height:66px;background:var(--band);color:var(--paper);text-align:center;font-size:16px;line-height:21px;padding-top:12px}
.photo{width:100%}
.cover-photo{height:220px;background:linear-gradient(180deg,#6f93c4 0%,#a8bcd6 35%,#8a6e52 55%,#6a5a45 72%,#4f7a35 100%)}
.features{height:104px;background:linear-gradient(180deg,#fff,#e9e9e9);padding:22px 0 0 30px;list-style:none}
.features li{display:flex;align-items:center;gap:10px;font-size:14px;color:var(--ink);margin-bottom:10px}
.features svg{flex:none}
.foot{position:absolute;left:0;bottom:0;width:100%;height:42px;background:var(--brown-dark);color:var(--paper);font-size:11px;display:flex;align-items:center;justify-content:center;gap:28px}

/* back cover */
.maps{height:180px;background:var(--paper-soft);display:flex;gap:12px;padding:14px}
.map{flex:1;background:linear-gradient(135deg,#f4f4f2,#dcdad6)}
.back-body{padding:34px 36px 0;text-align:center}
.back-name{font-size:30px;font-weight:700;letter-spacing:1px;color:var(--ink);margin-bottom:18px}
.back-lead{font-size:13px;font-weight:600;margin-bottom:8px}
.back-copy{font-size:10px;line-height:15px;color:var(--ink-soft);margin-bottom:26px}
.builder{display:flex;align-items:center;justify-content:center;gap:8px;font-size:14px;font-weight:600;color:var(--ink)}
.builder span.sq{width:14px;height:14px;background:var(--brown)}
.back-foot{justify-content:space-between;padding:0 22px;gap:0}

/* inside */
.forest{height:190px;background:linear-gradient(180deg,#3e5a2c 0%,#6d8c4a 45%,#8fa06a 70%,#5b6f3b 100%)}
.copy{padding:18px 28px 0}
.copy h3{font-size:12px;font-weight:600;color:var(--brown);margin:8px 0 3px}
.copy p{font-size:9px;line-height:13px;color:var(--ink-soft)}
.community{position:absolute;left:0;top:0;width:160px;height:518px;padding:20px 14px 0 20px}
.community h2{font-size:16px;line-height:19px;font-weight:400;color:var(--ink);margin-bottom:10px}
.lots{width:100%;border-collapse:collapse;font-size:8px;color:var(--ink-soft)}
.lots th{background:var(--band);color:var(--paper);font-weight:600;padding:2px 3px;text-align:left}
.lots td{padding:0 3px;line-height:10.4px;border-bottom:1px solid #ececec}
.aerial{position:absolute;right:0;top:0;width:270px;height:518px;background:linear-gradient(160deg,#2f4a25 0%,#4d6a3a 40%,#5f7b47 70%,#3d5530 100%)}
</style>
</head>
<body>
<div class="canvas">

  <!-- Front cover -->
  <section class="page front-cover" style="left:385px;top:150px">
    <header class="cover-head"><span class="brand-mark"></span><span class="brand-name">MAPLECREST HOLLOW</span></header>
    <div class="tagline">Introducing Alderton’s newest Luxury<br>New Home Community</div>
    <div class="photo cover-photo" role="img" aria-label="Photograph of a large stone luxury home with landscaped lawn under a blue sky"></div>
    <ul class="features">
      <li><svg width="12" height="12" viewBox="0 0 12 12"><circle cx="6" cy="6" r="5.5" fill="#8e8a87"/><path d="M5 3.5 7.5 6 5 8.5" stroke="#fff" stroke-width="1.4" fill="none"/></svg>Custom Homes from $1 Million</li>
      <li><svg width="12" height="12" viewBox="0 0 12 12"><circle cx="6" cy="6" r="5.5" fill="#8e8a87"/><path d="M5 3.5 7.5 6 5 8.5" stroke="#fff" stroke-width="1.4" fill="none"/></svg>36 Heavily Wooded Estate Sized Lots</li>
    </ul>
    <footer class="foot">www.MaplecrestHollowNB.com</footer>
  </section>

  <!-- Outside spread: back cover + front cover -->
  <section class="spread outside" style="top:880px">
    <div class="page left back-cover">
      <div class="maps">
        <div class="map" role="img" aria-label="Street map showing the community location"></div>
        <div class="map" role="img" aria-label="Regional highway map showing the community location"></div>
      </div>
      <div class="back-body">
        <div class="back-name">MAPLECREST HOLLOW</div>
        <p class="back-lead">Conveniently located just west of Route 9 and 140th Street, Alderton</p>
        <p class="back-copy">A quiet wooded setting close to top schools, parks, shopping and dining, with easy access to major highways and the wider metro area.</p>
        <div class="builder"><span class="sq"></span>Northgate Builders</div>
      </div>
      <footer class="foot back-foot"><span>sales@maplecresthollow.com</span><span>(555) 014-2290</span><span>MaplecrestHollowNB.com</span></footer>
    </div>
    <div class="page right front-cover">
      <header class="cover-head"><span class="brand-mark"></span><span class="brand-name">MAPLECREST HOLLOW</span></header>
      <div class="tagline">Introducing Alderton’s newest Luxury<br>New Home Community</div>
      <div class="photo cover-photo" role="img" aria-label="Photograph of a large stone luxury home with landscaped lawn under a blue sky"></div>
      <ul class="features">
        <li><svg width="12" height="12" viewBox="0 0 12 12"><circle cx="6" cy="6" r="5.5" fill="#8e8a87"/><path d="M5 3.5 7.5 6 5 8.5" stroke="#fff" stroke-width="1.4" fill="none"/></svg>Custom Homes from $1 Million</li>
        <li><svg width="12" height="12" viewBox="0 0 12 12"><circle cx="6" cy="6" r="5.5" fill="#8e8a87"/><path d="M5 3.5 7.5 6 5 8.5" stroke="#fff" stroke-width="1.4" fill="none"/></svg>36 Heavily Wooded Estate Sized Lots</li>
      </ul>
      <footer class="foot">www.MaplecrestHollowNB.com</footer>
    </div>
  </section>

  <!-- Inside spread -->
  <section class="spread inside" style="top:1680px">
    <div class="page left">
      <div class="photo forest" role="img" aria-label="Photographs of woodland trees, a creek and deer in the community park"></div>
      <div class="copy">
        <h3>Nature Driven Design</h3>
        <p>Every street and homesite follows the natural land, keeping mature trees, rolling hills and open views at the heart of the neighborhood plan.</p>
        <h3>Preservation and Conservation</h3>
        <p>Wooded buffers and protected green space surround the lots, so wildlife, creeks and old growth trees remain part of daily life for residents.</p>
        <h3>11 Acre Private Park</h3>
        <p>A private park with walking trails, a stream and quiet seating areas offers a peaceful retreat reserved for homeowners and their guests.</p>
        <h3>Custom Homes</h3>
        <p>Each residence is built to order by skilled builders, with thoughtful design and fine materials that suit the setting and your way of living.</p>
      </div>
      <footer class="foot">www.MaplecrestHollowNB.com</footer>
    </div>
    <div class="page right">
      <div class="community">
        <h2>A COMMUNITY<br>LIKE NO OTHER</h2>
        <table class="lots">
          <thead><tr><th>Lot</th><th>Sq. Feet</th><th>Acres</th></tr></thead>
          <tbody>
            <tr><td>1</td><td>21,650</td><td>0.50</td></tr>
            <tr><td>2</td><td>23,410</td><td>0.54</td></tr>
            <tr><td>3</td><td>24,980</td><td>0.57</td></tr>
            <tr><td>4</td><td>22,300</td><td>0.51</td></tr>
            <tr><td>5</td><td>26,120</td><td>0.60</td></tr>
            <tr><td>6</td><td>27,840</td><td>0.64</td></tr>
            <tr><td>7</td><td>25,760</td><td>0.59</td></tr>
            <tr><td>8</td><td>30,210</td><td>0.69</td></tr>
            <tr><td>9</td><td>28,450</td><td>0.65</td></tr>
            <tr><td>10</td><td>31,900</td><td>0.73</td></tr>
            <tr><td>11</td><td>29,370</td><td>0.67</td></tr>
            <tr><td>12</td><td>33,480</td><td>0.77</td></tr>
            <tr><td>13</td><td>35,020</td><td>0.80</td></tr>
            <tr><td>14</td><td>32,640</td><td>0.75</td></tr>
            <tr><td>15</td><td>36,810</td><td>0.85</td></tr>
            <tr><td>16</td><td>38,260</td><td>0.88</td></tr>
            <tr><td>17</td><td>34,590</td><td>0.79</td></tr>
            <tr><td>18</td><td>40,120</td><td>0.92</td></tr>
            <tr><td>19</td><td>37,430</td><td>0.86</td></tr>
            <tr><td>20</td><td>42,780</td><td>0.98</td></tr>
            <tr><td>21</td><td>39,950</td><td>0.92</td></tr>
            <tr><td>22</td><td>44,310</td><td>1.02</td></tr>
            <tr><td>23</td><td>41,670</td><td>0.96</td></tr>
            <tr><td>24</td><td>46,880</td><td>1.08</td></tr>
            <tr><td>25</td><td>43,220</td><td>0.99</td></tr>
            <tr><td>26</td><td>48,540</td><td>1.11</td></tr>
            <tr><td>27</td><td>45,760</td><td>1.05</td></tr>
            <tr><td>28</td><td>51,030</td><td>1.17</td></tr>
            <tr><td>29</td><td>47,390</td><td>1.09</td></tr>
            <tr><td>30</td><td>53,620</td><td>1.23</td></tr>
            <tr><td>31</td><td>49,810</td><td>1.14</td></tr>
            <tr><td>32</td><td>55,470</td><td>1.27</td></tr>
            <tr><td>33</td><td>52,260</td><td>1.20</td></tr>
            <tr><td>34</td><td>58,900</td><td>1.35</td></tr>
            <tr><td>35</td><td>54,130</td><td>1.24</td></tr>
            <tr><td>36</td><td>61,740</td><td>1.42</td></tr>
          </tbody>
        </table>
      </div>
      <div class="aerial" role="img" aria-label="Aerial photograph of the wooded site with the lot plan and curving streets overlaid"></div>
      <footer class="foot">www.MaplecrestHollowNB.com</footer>
    </div>
  </section>

</div>
</body>
</html>
```